BRIGHT COLORFUL + 55 FAMILY HISTORY BROCHURE 11 x 17 bifold

11 x 17 Bifold Flyer I have given you the Layout I just need you to make it Pretty

YOU DO NOT NEED TO FOLLOW MY LAYOUT, You can but dont have too

Target Market(s)

55 year old consumers, who could choose our service of Hereditary Cancer Screening

Industry/Entity Type

Health And Wellness

Requirements
Must have
• Must be appealing to Grand Parents, must make them want to test , show lots of pictures of grand children, YOU DO NOT NEED TO FOLLOW MY LAYOUT , You can but dont have too
Nice to have
• use our colors of our logo , YOU DO NOT NEED TO FOLLOW MY LAYOUT , You can but dont have too
Should not have
• YOU DO NOT NEED TO FOLLOW MY LAYOUT, You can but dont have too

```html
<!DOCTYPE html>
<html lang="en">
<head>
<meta charset="utf-8">
<title>Meridian Kin Health – Family Cancer Screening Brochure</title>
<link href="https://fonts.googleapis.com/css2?family=Montserrat:wght@300;400;700&family=Poiret+One&display=swap" rel="stylesheet">
<style>
  :root {
    --lime: #86f510;
    --navy: #0b1263;
    --ink: #4a4a4a;
    --paper: #ffffff;
    --faint-lime: #eef9df;
    --photo-warm: #d9cfc6;
    --photo-green: #7fa35a;
    --display: "Poiret One", "Montserrat", sans-serif;
    --body: "Montserrat", Arial, sans-serif;
  }
  * { box-sizing: border-box; margin: 0; padding: 0; }
  html, body { width: 1200px; height: 1200px; overflow: hidden; background: #f4f4f4; }
  .sheet {
    position: absolute; left: 0; top: 174px; width: 1200px; height: 851px;
    background: var(--paper); overflow: hidden; font-family: var(--body); color: var(--ink);
  }
  .abs { position: absolute; }
  .copy { font-size: 10.5px; font-weight: 300; line-height: 13.3px; text-align: justify; }
  .copy p + p { margin-top: 4px; }
  .bullets { list-style: none; font-size: 10.5px; font-weight: 300; line-height: 13.3px; }
  .bullets li { position: relative; padding-left: 12px; }
  .bullets li::before {
    content: ""; position: absolute; left: 0; top: 3px; width: 7px; height: 7px; background: var(--lime);
  }
  .display { font-family: var(--display); text-transform: uppercase; letter-spacing: 1px; }

  .cta-band {
    left: 419px; top: 76px; width: 781px; height: 52px; background: var(--lime);
    font-size: 29px; font-weight: 300; color: #f3ffe6; padding-left: 22px; line-height: 52px; white-space: nowrap;
  }
  .cta-band .url { color: var(--navy); font-weight: 400; }
  .brand-bar {
    left: 653px; top: 128px; width: 499px; height: 42px; background: var(--navy);
    color: #fff; font-size: 30px; text-align: center; line-height: 44px;
  }
  .stat-head { left: 58px; top: 298px; font-size: 27px; line-height: 31px; color: var(--lime); }
  .stat-head strong { font-family: var(--body); font-weight: 700; color: var(--navy); letter-spacing: 0; }
  .tagline { left: 58px; top: 430px; font-size: 10.5px; font-weight: 300; }
  .pictogram {
    left: 367px; top: 298px; width: 196px; height: 136px;
    background: linear-gradient(135deg, #e9e9e9, #eef9df); border-radius: 4px;
  }
  .get-tested { left: 1010px; top: 224px; width: 133px; text-align: right; font-size: 31px; line-height: 51px; }
  .why { left: 637px; top: 396px; font-size: 31px; line-height: 51px; }
  .navy-text { color: var(--navy); }
  .lime-text { color: var(--lime); }
  .closing { left: 636px; top: 518px; font-size: 10.5px; font-weight: 300; line-height: 13.3px; width: 320px; }
  .brand-mark { left: 1058px; top: 524px; display: flex; align-items: center; gap: 5px; }
  .brand-mark .dot { width: 22px; height: 22px; border-radius: 50%; background: var(--navy); }
  .brand-mark span { font-size: 8.5px; font-weight: 700; color: var(--navy); line-height: 9px; width: 46px; }

  .photo { top: 581px; height: 230px; }
  .photo-grandparents { left: 52px; width: 367px; background: linear-gradient(120deg, #e6dcd3, #cdbfb4 55%, #b8b1ad); }
  .photo-family { left: 784px; width: 349px; background: linear-gradient(160deg, #a8c580, #7fa35a 60%, #8fb4cf); }
  .navy-panel { top: 581px; height: 230px; background: var(--navy); }
  .panel-a { left: 425px; width: 176px; }
  .panel-b { left: 603px; width: 177px; }
  .decor { left: 0; top: 0; width: 1200px; height: 851px; pointer-events: none; }
</style>
</head>
<body>
<main class="sheet">

  <div class="abs copy" style="left:58px; top:76px; width:335px;">
    <p>Genetic Testing is done to determine whether family members without obvious illness have inherited the same mutation as a family member who is known to carry a cancer associated mutation. Meaning Will You Help Your Kids &amp; <span style="display:block;text-align:center">Grand Children</span></p>
  </div>

  <div class="abs cta-band">To Get Started, Visit <span class="url">kinhealthcheck.com</span></div>
  <div class="abs brand-bar display">Meridian Kin Health</div>

  <div class="abs copy" style="left:58px; top:163px; width:506px;">
    <p>There are many benefits to getting tested, regardless of the eventual result. If one of your family members however distant had cancer, there is a chance that you inherited a gene mutation that not only increases your personal risk of cancer, but also could be passed to the next generation. By tetsing, you can</p>
  </div>

  <ul class="abs bullets" style="left:82px; top:228px;">
    <li>Potentially prevent cancer.</li>
    <li>Delay the onset of cancer.</li>
    <li>Catch cancer at the early stage.</li>
  </ul>

  <h2 class="abs display stat-head"><strong>15%</strong> of cancer<br>is caused<br>by gene<br>mutations</h2>
  <p class="abs tagline">“The Power of Knowledge”</p>

  <div class="abs pictogram" role="img" aria-label="Family tree pictogram of figures across three generations, some highlighted in green as gene carriers"></div>

  <div class="abs copy" style="left:58px; top:478px; width:499px;">
    <p>Helping Younger Family Members Know if there is a Risk and Preparing for it. Knowing if you have a genetic mutation is that you can work with your doctor to monitor and address your cancer risks. According to the National Wellness Council eating 5 or more servings of vegetables, fruits and Most Importantly also lowering your intake of red meat, dairy and <span style="display:block;text-align:center">eggs will help prevent or delay cancer.</span></p>
  </div>

  <div class="abs copy" style="left:643px; top:192px; width:500px; text-align:left;">
    <p>Your decision won’t just affect you, it will also impact your family, since your test results may forecast their cancer risks, too.</p>
  </div>

  <div class="abs copy" style="left:643px; top:224px; width:364px;">
    <p>We believe it is important to understand what can and cannot be learned with genetic testing. Genetic mutations can increase risks for certain cancers, but this does not mean cancer will definitely develop. You should be prepared to receive positive or negative results. Most people receive negative results meaning no mutations associated with an increased risk for the hereditary cancers.</p>
    <p>Our testing requires only a simple swab of the inside of a patient’s cheek totest for DNA mutations. our test covers the main 8 cancers; Breast, melanoma, ovarian, pancreatic, prostrate, uterine, colorectal and stomach cancers.</p>
  </div>

  <h2 class="abs display get-tested"><span class="navy-text">Get</span><br><span class="lime-text">Tested</span><br><span class="lime-text">Today</span></h2>

  <h2 class="abs display why"><span class="navy-text">Why Get</span><br><span class="lime-text">Tested ?</span></h2>

  <ul class="abs bullets" style="left:838px; top:403px;">
    <li>0 Cost to Most.</li>
    <li>1 Test, 134 Genes.</li>
    <li>Timely Results.</li>
    <li>Cancer is Observed Earlier.</li>
    <li>Early Treatment.</li>
    <li>Non-Intrusive Test.</li>
  </ul>

  <p class="abs closing">Give Them the Gift of Knowledge, knowing is better than not knowing. Knowledge is Power</p>

  <div class="abs brand-mark"><div class="dot"></div><span>MERIDIAN KIN HEALTH</span></div>

  <div class="abs photo photo-grandparents" role="img" aria-label="Photo of smiling grandparents with their two grandchildren"></div>
  <div class="abs navy-panel panel-a"></div>
  <div class="abs navy-panel panel-b"></div>
  <div class="abs photo photo-family" role="img" aria-label="Photo of a three-generation family standing together outdoors in a park"></div>

  <svg class="abs decor" viewBox="0 0 1200 851" aria-hidden="true">
    <circle cx="1196" cy="431" r="56" fill="none" stroke="var(--faint-lime)" stroke-width="18"/>
    <circle cx="419" cy="696" r="43" fill="var(--lime)" stroke="#fff" stroke-width="3"/>
    <circle cx="779" cy="696" r="43" fill="var(--lime)" stroke="#fff" stroke-width="3"/>
  </svg>

</main>
</body>
</html>
```